CareerHUB Background Image Needed

I need a CareerHUB background image for my personal CareerHUB profile page. The dimension is 1400 pixels wide X 350 pixels high.

I am a consultant for www.RedMapleRun.com. The logo files are located here:

https://www.filecrate.net/sh/q7m3vtx2lpe8nwc4rbyaz/k?key=gn5wd2pxkv9tjhm4caqe81lr3&v=0

A single message in the background is:

"Give your business a Red Maple Run with a proven path to optimized sales"

```html
<!DOCTYPE html>
<html lang="en">
<head>
<meta charset="utf-8">
<title>Red Maple Run – CareerHUB Profile Background</title>
<link rel="stylesheet" href="https://fonts.googleapis.com/css2?family=Montserrat:wght@400;500;800;900&display=swap">
<style>
  :root {
    --page-bg: #d6d6d6;
    --navy-deep: #071d33;
    --navy: #0b2f4d;
    --teal: #0f5a7c;
    --glow: #1f8fb8;
    --orange: #ee6a21;
    --white: #ffffff;
  }
  * { margin: 0; padding: 0; box-sizing: border-box; }
  html, body {
    width: 1200px;
    height: 1071px;
    overflow: hidden;
    background: var(--page-bg);
    font-family: "Montserrat", sans-serif;
  }
  .banner {
    position: absolute;
    left: 0;
    top: 385px;
    width: 1200px;
    height: 300px;
    overflow: hidden;
    color: var(--white);
  }
  .banner__backdrop {
    position: absolute;
    inset: 0;
    background:
      radial-gradient(ellipse at 88% 40%, rgba(31,143,184,0.45), transparent 45%),
      radial-gradient(ellipse at 12% 70%, rgba(31,143,184,0.35), transparent 40%),
      linear-gradient(180deg, var(--navy) 0%, var(--teal) 55%, var(--navy-deep) 100%);
  }
  .brand {
    position: absolute;
    left: 40px;
    top: 30px;
    display: flex;
    align-items: center;
    gap: 14px;
  }
  .brand__dot {
    width: 46px;
    height: 46px;
    border-radius: 50%;
    background: var(--orange);
    flex: none;
  }
  .brand__name {
    font-weight: 900;
    font-size: 27px;
    line-height: 0.95;
    text-transform: uppercase;
    color: var(--white);
  }
  .web-tab {
    position: absolute;
    right: 0;
    top: 44px;
    height: 26px;
    padding: 0 10px 0 28px;
    background: var(--orange);
    clip-path: polygon(0 0, 100% 0, 100% 100%, 14px 100%);
    font-size: 14px;
    font-weight: 400;
    line-height: 26px;
    color: var(--white);
  }
  .web-tab strong { font-weight: 800; }
  .headline {
    position: absolute;
    left: 310px;
    top: 50px;
    text-transform: uppercase;
  }
  .headline__line {
    display: block;
    font-size: 36px;
    line-height: 1.15;
    font-weight: 400;
    white-space: nowrap;
  }
  .headline__line strong { font-weight: 800; }
  .headline__highlight {
    display: inline-block;
    margin: 6px 0 10px;
    padding: 0 16px;
    height: 64px;
    background: var(--orange);
    font-size: 58px;
    line-height: 66px;
    font-weight: 900;
    letter-spacing: 0.5px;
    white-space: nowrap;
  }
</style>
</head>
<body>
  <section class="banner" aria-label="Red Maple Run profile background">
    <div class="banner__backdrop" role="img" aria-label="Dark blue city skyline with glowing network lines and dots"></div>

    <div class="brand">
      <span class="brand__dot"></span>
      <span class="brand__name">Red<br>Maple<br>Run</span>
    </div>

    <div class="web-tab">www.<strong>redmaplerun</strong>.com</div>

    <h1 class="headline">
      <span class="headline__line">Give your <strong>business</strong></span>
      <span class="headline__highlight">A Red Maple Run</span>
      <span class="headline__line">With <strong>a proven path to</strong></span>
      <span class="headline__line"><strong>Optimized sales</strong></span>
    </h1>
  </section>
</body>
</html>
```